I own a rendering company which is in the construction industry i already have a logo i would like i

I want to make the website look professional and blends nicely with the logo, if i can have contact information and photos logos and a place where they can email me for job quotes or request and we want to win the big jobs so think also corporate in conjunction with construction. also an area for brief description and about us

Target Market(s)

Home owners/Investors, Small and major construction companies

Industry/Entity Type

Construction Company

Font styles to use
Serif
Sans Serif

Colors

Designer to choose colors to be used in the design.

Requirements
Must have
• An area for pictures to show with fade changes or clicking options(of white set walls, acrylic render expensive houses walls) an "about us" section. An area to where potential customers can email us (a writing box) where we can receive request for quotes and potential jobs. all contact information and license numbers
Nice to have
• pictures of plastered walls (posh elegant) and rendered walls acrylic and cement render
Should not have
• anything boring plain font etc

```html
<!DOCTYPE html>
<html lang="en">
<head>
<meta charset="utf-8">
<title>Kestrel Rendering</title>
<link href="https://fonts.googleapis.com/css2?family=EB+Garamond:wght@400;500;600&family=Arimo:wght@400;700&display=swap" rel="stylesheet">
<style>
:root{
  --red:#ec1c24;
  --red-dark:#c3161d;
  --ink:#555a5e;
  --text:#5f5f5f;
  --grey-band:#e9e9e9;
  --footer:#676767;
  --footer-dark:#4f4f4f;
  --white:#ffffff;
  --serif:"EB Garamond", Georgia, serif;
  --sans:"Arimo", Arial, sans-serif;
}
*{box-sizing:border-box;margin:0;padding:0}
html,body{width:1200px;height:2575px;overflow:hidden;background:var(--white)}
body{position:relative;font-family:var(--sans);color:var(--text)}

/* header */
.site-header{position:absolute;left:0;top:0;width:1200px;height:125px;background:var(--white);z-index:3}
.brand{position:absolute;left:77px;top:0;width:177px;height:157px;background:var(--white);box-shadow:0 2px 8px rgba(0,0,0,.18);display:flex;flex-direction:column;align-items:center;justify-content:center;gap:10px}
.brand-mark{width:30px;height:30px;border-radius:50%;background:var(--red)}
.brand-name{font-family:var(--serif);font-weight:500;color:var(--ink);font-size:24px;line-height:26px;text-align:center;width:120px}
.header-phone{position:absolute;left:722px;top:18px;display:flex;align-items:center;gap:14px;font-size:18px;color:#333}
.round{display:inline-flex;align-items:center;justify-content:center;border-radius:50%}
.header-phone .round{width:40px;height:40px;background:var(--red)}
.header-social{position:absolute;left:936px;top:18px;display:flex;gap:8px}
.header-social .round{width:40px;height:40px;background:var(--red);color:var(--white)}
.main-nav{position:absolute;top:84px;left:776px;display:flex;gap:38px;font-size:18px;color:#444}
.main-nav .active{color:var(--red)}

/* hero */
.hero{position:absolute;left:0;top:125px;width:1200px;height:620px}
.hero-photo{position:absolute;inset:0;background:linear-gradient(115deg,#d9d9d8 0%,#c9c9c7 35%,#e6e6e4 60%,#bdbdbb 100%)}
.hero-title{position:absolute;left:79px;top:218px;font-family:var(--serif);font-weight:500;font-size:46px;color:#2b2b2b;letter-spacing:1px}
.hero-lead{position:absolute;left:79px;top:288px;width:560px;font-size:17.5px;line-height:28px;color:#333}
.hero-curve{position:absolute;left:0;top:470px}

/* about */
.about{position:absolute;left:0;top:745px;width:1200px;text-align:center}
.section-title{font-family:var(--serif);font-weight:500;font-size:40px;color:var(--ink);text-align:center}
.section-title em{font-style:normal;color:var(--red)}
.about .section-title{margin-top:34px}
.about p{width:810px;margin:16px auto 0;font-size:14.5px;line-height:25px;color:var(--text)}
.about p + p{margin-top:12px}

/* services */
.services{position:absolute;left:0;top:1064px;width:1200px;height:498px;background:var(--grey-band)}
.services .section-title{margin-top:38px}
.service-card{position:absolute;top:109px;width:323px;height:321px;background:var(--white);box-shadow:0 1px 5px rgba(0,0,0,.15);text-align:center}
.service-card:nth-of-type(1){left:77px}
.service-card:nth-of-type(2){left:439px}
.service-card:nth-of-type(3){left:800px}
.service-photo{margin:10px 10px 0;height:176px}
.service-card h3{font-family:var(--serif);font-weight:400;font-size:26px;color:#555;margin-top:20px}
.service-card p{font-size:14.5px;line-height:26px;color:#666;padding:0 20px;margin-top:4px}

/* quote */
.quote{position:absolute;left:0;top:1562px;width:1200px;height:315px;background:var(--red);color:var(--white)}
.quote-intro{position:absolute;right:644px;top:82px;text-align:right;width:400px}
.quote-intro h2{font-family:var(--serif);font-weight:500;font-size:36px}
.quote-intro p{font-size:14.5px;line-height:25px;margin-top:12px;margin-left:25px}
.field{position:absolute;background:var(--red-dark);border-radius:3px;color:var(--white);font-size:15px;padding:13px 12px;height:45px}
.field-name{left:585px;top:90px;width:248px}
.field-email{left:845px;top:90px;width:249px}
.field-subject{left:585px;top:146px;width:509px}
.submit{position:absolute;left:585px;top:204px;width:165px;height:52px;background:var(--white);color:var(--red);border-radius:3px;font-family:var(--serif);font-weight:600;font-size:20px;letter-spacing:1px;display:flex;align-items:center;justify-content:center}

/* testimonials */
.testimonials{position:absolute;left:0;top:1877px;width:1200px}
.testimonials .section-title{margin-top:36px}
.testimonial{position:absolute;top:118px;width:480px}
.testimonial:nth-of-type(1){left:77px}
.testimonial:nth-of-type(2){left:638px}
.testimonial blockquote{position:relative;padding-left:28px;font-size:14.5px;line-height:25px;color:#666}
.quote-mark{position:absolute;font-family:var(--serif);font-weight:700;font-size:36px;color:#777;line-height:1}
.quote-open{left:0;top:-3px}
.quote-close{left:355px;top:47px}
.client{display:flex;align-items:center;gap:12px;margin:24px 0 0 29px;font-size:15px;color:#666}
.avatar{width:66px;height:66px;border-radius:50%;border:3px solid #d8d8d8;background:linear-gradient(160deg,#e9d8c9,#b89f8c)}
.divider{position:absolute;left:599px;top:2002px;width:1px;height:135px;background:#d0d0d0}

/* footer */
.site-footer{position:absolute;left:0;top:2190px;width:1200px;height:385px;background:var(--footer);color:var(--white)}
.footer-curve{position:absolute;left:0;top:0}
.footer-nav{position:absolute;left:81px;top:169px;display:flex;gap:44px;font-size:15px}
.footer-social{position:absolute;left:983px;top:160px;display:flex;gap:8px}
.footer-social .round{width:40px;height:40px;background:var(--footer-dark);color:var(--white)}
.footer-social .round:first-child{background:var(--white);color:var(--footer-dark)}
.contact-row{position:absolute;top:246px;display:flex;align-items:center;gap:14px;font-size:15px;line-height:22px}
.contact-row .round{width:44px;height:44px;background:var(--footer-dark);flex:none}
.contact-address{left:81px}
.contact-phone{left:398px}
.contact-email{left:648px}
.copyright{position:absolute;left:0;top:338px;width:1200px;text-align:center;font-size:15px}
.to-top{position:absolute;left:1138px;top:312px;width:52px;height:52px;border:2px solid var(--white)}
</style>
</head>
<body>

<header class="site-header">
  <div class="brand">
    <div class="brand-mark"></div>
    <div class="brand-name">Kestrel Rendering</div>
  </div>
  <div class="header-phone">
    <span class="round"><svg width="20" height="20" viewBox="0 0 24 24"><path fill="#fff" d="M6.6 10.8a15.1 15.1 0 0 0 6.6 6.6l2.2-2.2c.3-.3.7-.4 1-.2 1.1.4 2.3.6 3.6.6.6 0 1 .4 1 1V20c0 .6-.4 1-1 1C10.6 21 3 13.4 3 4c0-.6.4-1 1-1h3.5c.6 0 1 .4 1 1 0 1.3.2 2.5.6 3.6.1.3 0 .7-.2 1z"/></svg></span>
    123 456 7890
  </div>
  <div class="header-social" aria-label="Social links">
    <span class="round" aria-label="Share"><svg width="18" height="18" viewBox="0 0 24 24" fill="none" stroke="currentColor" stroke-width="2"><circle cx="18" cy="5" r="2.5"/><circle cx="6" cy="12" r="2.5"/><circle cx="18" cy="19" r="2.5"/><path d="M8.2 10.8l7.6-4.5M8.2 13.2l7.6 4.5"/></svg></span>
    <span class="round" aria-label="Link"><svg width="18" height="18" viewBox="0 0 24 24" fill="none" stroke="currentColor" stroke-width="2"><path d="M10 14a4 4 0 0 0 5.7 0l3-3a4 4 0 0 0-5.7-5.7l-1.2 1.2M14 10a4 4 0 0 0-5.7 0l-3 3a4 4 0 0 0 5.7 5.7l1.2-1.2"/></svg></span>
    <span class="round" aria-label="Message"><svg width="18" height="18" viewBox="0 0 24 24" fill="none" stroke="currentColor" stroke-width="2"><path d="M4 5h16v11H9l-5 4z"/></svg></span>
    <span class="round" aria-label="Website"><svg width="18" height="18" viewBox="0 0 24 24" fill="none" stroke="currentColor" stroke-width="2"><circle cx="12" cy="12" r="9"/><path d="M3 12h18M12 3c3 3 3 15 0 18M12 3c-3 3-3 15 0 18"/></svg></span>
  </div>
  <nav class="main-nav">
    <span class="active">Home</span><span>About</span><span>Services</span><span>Contact</span>
  </nav>
</header>

<section class="hero">
  <div class="hero-photo" role="img" aria-label="Tradesman in a hard hat rendering a white wall with a trowel"></div>
  <h1 class="hero-title">KESTREL RENDERING</h1>
  <p class="hero-lead">Lorem Ipsum is simply dummy text of the printing and typesetting industry. Lorem Ipsum has been the industry.</p>
  <svg class="hero-curve" width="1200" height="150" viewBox="0 0 1200 150">
    <path fill="#fff" d="M0,110 C250,150 480,40 760,12 C950,-5 1120,20 1200,55 L1200,150 L0,150 Z"/>
    <path fill="#ec1c24" d="M425,128 C650,45 960,15 1200,115 L1200,150 C980,60 720,75 425,131 Z"/>
  </svg>
</section>

<section class="about">
  <h2 class="section-title">Who <em>We Are</em></h2>
  <p>There are many variations of passages of Lorem Ipsum available, but the majority have suffered alteration in some form, by injected humour, or randomised words which don't look even slightly believable. If you are going to use a passage of Lorem Ipsum, you need to be sure there isn't anything embarrassing hidden in the middle of text</p>
  <p>. All the Lorem Ipsum generators on the Internet tend to repeat predefined chunks as necessary, making this the first true generator on the Internet. It uses a dictionary of over 200 Latin words, combined with a handful of model sentence structures, to generate Lorem Ipsum which looks reasonable.</p>
</section>

<section class="services">
  <h2 class="section-title">Services <em>We Provide</em></h2>
  <article class="service-card">
    <div class="service-photo" role="img" aria-label="Hand applying acrylic render to a wall with a float" style="background:linear-gradient(120deg,#b9b7b2,#8f8d88)"></div>
    <h3>Rendered walls acrylic</h3>
    <p>Lorem Ipsum is simply dummy text of the printing and typesetting industry.</p>
  </article>
  <article class="service-card">
    <div class="service-photo" role="img" aria-label="Plaster being sprayed onto a block wall" style="background:linear-gradient(120deg,#3f3f3f,#6c6a62 55%,#e6e0c8)"></div>
    <h3>Plastered walls</h3>
    <p>Lorem Ipsum is simply dummy text of the printing and typesetting industry.</p>
  </article>
  <article class="service-card">
    <div class="service-photo" role="img" aria-label="Gloved hand spreading cement render with a trowel" style="background:linear-gradient(120deg,#a7a6a3,#d4d3d0 50%,#8e8d8a)"></div>
    <h3>Cement render</h3>
    <p>Lorem Ipsum is simply dummy text of the printing and typesetting industry.</p>
  </article>
</section>

<section class="quote">
  <div class="quote-intro">
    <h2>Request A Free Quote</h2>
    <p>Please feel free to contact us at the information provided below and we will be sure to get back to you as soon as possible.</p>
  </div>
  <div class="field field-name">Name</div>
  <div class="field field-email">Email</div>
  <div class="field field-subject">Subject</div>
  <div class="submit">SUBMIT</div>
</section>

<section class="testimonials">
  <h2 class="section-title">What Our <em>Client Say About Us</em></h2>
  <div class="testimonial">
    <blockquote><span class="quote-mark quote-open">&ldquo;</span>Lorem Ipsum is simply dummy text of the printing and typesetting industry. Lorem Ipsum has been the industry's standard dummy text ever since the 1500s.<span class="quote-mark quote-close">&rdquo;</span></blockquote>
    <div class="client"><span class="avatar" role="img" aria-label="Client portrait"></span>- Client Name</div>
  </div>
  <div class="testimonial">
    <blockquote><span class="quote-mark quote-open">&ldquo;</span>Lorem Ipsum is simply dummy text of the printing and typesetting industry. Lorem Ipsum has been the industry's standard dummy text ever since the 1500s.<span class="quote-mark quote-close">&rdquo;</span></blockquote>
    <div class="client"><span class="avatar" role="img" aria-label="Client portrait"></span>- Client Name</div>
  </div>
</section>
<div class="divider"></div>

<footer class="site-footer">
  <svg class="footer-curve" width="1200" height="150" viewBox="0 0 1200 150">
    <path fill="#fff" d="M0,0 H1200 V18 C1060,110 820,145 610,112 C400,80 200,-5 0,38 Z"/>
    <path fill="#ec1c24" d="M425,45 C680,125 980,120 1200,5 L1200,28 C990,140 700,145 425,50 Z"/>
  </svg>
  <nav class="footer-nav"><span>Home</span><span>About</span><span>Services</span><span>Contact</span></nav>
  <div class="footer-social" aria-label="Social links">
    <span class="round" aria-label="Share"><svg width="18" height="18" viewBox="0 0 24 24" fill="none" stroke="currentColor" stroke-width="2"><circle cx="18" cy="5" r="2.5"/><circle cx="6" cy="12" r="2.5"/><circle cx="18" cy="19" r="2.5"/><path d="M8.2 10.8l7.6-4.5M8.2 13.2l7.6 4.5"/></svg></span>
    <span class="round" aria-label="Link"><svg width="18" height="18" viewBox="0 0 24 24" fill="none" stroke="currentColor" stroke-width="2"><path d="M10 14a4 4 0 0 0 5.7 0l3-3a4 4 0 0 0-5.7-5.7l-1.2 1.2M14 10a4 4 0 0 0-5.7 0l-3 3a4 4 0 0 0 5.7 5.7l1.2-1.2"/></svg></span>
    <span class="round" aria-label="Website"><svg width="18" height="18" viewBox="0 0 24 24" fill="none" stroke="currentColor" stroke-width="2"><circle cx="12" cy="12" r="9"/><path d="M3 12h18M12 3c3 3 3 15 0 18M12 3c-3 3-3 15 0 18"/></svg></span>
  </div>
  <div class="contact-row contact-address">
    <span class="round"><svg width="18" height="18" viewBox="0 0 24 24"><path fill="#fff" d="M12 2a7 7 0 0 0-7 7c0 5.2 7 13 7 13s7-7.8 7-13a7 7 0 0 0-7-7zm0 9.5A2.5 2.5 0 1 1 12 6.5a2.5 2.5 0 0 1 0 5z"/></svg></span>
    <span>Lorem Ipsum is simply dummy<br>text of the printing.</span>
  </div>
  <div class="contact-row contact-phone">
    <span class="round"><svg width="18" height="18" viewBox="0 0 24 24"><path fill="#fff" d="M6.6 10.8a15.1 15.1 0 0 0 6.6 6.6l2.2-2.2c.3-.3.7-.4 1-.2 1.1.4 2.3.6 3.6.6.6 0 1 .4 1 1V20c0 .6-.4 1-1 1C10.6 21 3 13.4 3 4c0-.6.4-1 1-1h3.5c.6 0 1 .4 1 1 0 1.3.2 2.5.6 3.6.1.3 0 .7-.2 1z"/></svg></span>
    <span>123 456 7890</span>
  </div>
  <div class="contact-row contact-email">
    <span class="round"><svg width="18" height="18" viewBox="0 0 24 24"><path fill="#fff" d="M3 5h18v14H3z"/><path fill="none" stroke="#4f4f4f" stroke-width="1.6" d="M3 5l9 7 9-7"/></svg></span>
    <span>info@kestrelrendering.com</span>
  </div>
  <p class="copyright">2017 @KESTREL RENDERING. - All Rights Reserved</p>
  <span class="round to-top"><svg width="20" height="20" viewBox="0 0 24 24"><path fill="none" stroke="#fff" stroke-width="2.5" d="M5 15l7-7 7 7"/></svg></span>
</footer>

</body>
</html>
```